Need Pexora Ads for Tyre Company

Need some pexora ads graphics for our tyre company Wheel Mates that only operates in the cayman islands.

Need Ratio Ads: 1000x1000, 1910x1000, 300x600

Important things to have the customer know:
-Email : info@wheelmates-demo.ky
-Phone: +1 345 555 0187
-Address: 41 Palmetto Lane, George Town, Cayman Islands
-Website: wheelmates-demo.ky (Please see our website for the tyres we offer)
- Common Car brands that our Tyres are compatible with: Ravello, Korvexa, Pip Talvo, Bexiline, Vardo, Pelmoro, Quendra, Strandmobil
- Our tyres are priced from KYD$55-$60
-We offer free installation on tyres when customers come to our facility to get them changed.
-We sell tyres in bulk and individually.

*You can choose which things to add or omit for the best look, feel free to reword any of the above also to better fit in.
*Please keep in mind that these will have to be viewed in small formats aswell since they are for pexora ads. Please ensure everything is readable when zoomed out.

Target Market(s)

car rental companies & individuals who need to get their tyres replace

Industry/Entity Type

Automotive, Tyre replacement, Car Parts

Colors
EB3D1F
EC4F4E
F09395
F8D3D4
FCEDEE

Requirements
Must have
• Phone, Location, Brands that our tyres are compatible with, Same theme as our logo(Red & Black, White), design adapted to the 3 ratios listed above
Nice to have
• Creative advertising

```html
<!DOCTYPE html>
<html lang="en">
<head>
<meta charset="utf-8">
<title>Wheel Mates – Skyscraper Ad 300x600</title>
<link rel="stylesheet" href="https://fonts.googleapis.com/css2?family=Exo+2:wght@500;600;700&display=swap">
<style>
  :root {
    --brand-red: #e2261a;
    --ink-black: #060606;
    --tread-dark: #141414;
    --white: #ffffff;
    --rule-grey: #3a3a3a;
    --page: #ffffff;
  }
  html, body {
    margin: 0;
    padding: 0;
    width: 1200px;
    height: 1200px;
    overflow: hidden;
    background: var(--page);
    font-family: "Exo 2", sans-serif;
  }
  .ad {
    position: absolute;
    left: 450px;
    top: 300px;
    width: 300px;
    height: 600px;
    overflow: hidden;
    background: radial-gradient(ellipse at 50% 55%, var(--tread-dark) 0%, var(--ink-black) 70%);
    outline: 1px solid #000;
    color: var(--white);
  }
  .tread-backdrop {
    position: absolute;
    left: 0; top: 100px;
    width: 300px; height: 360px;
    background: linear-gradient(180deg, rgba(30,30,30,0.0) 0%, rgba(34,34,34,0.55) 55%, rgba(10,10,10,0) 100%);
  }
  .wordmark {
    position: absolute;
    top: 30px; left: 0; width: 300px;
    display: flex; align-items: center; justify-content: center; gap: 8px;
    font-size: 30px; font-weight: 700; color: var(--white);
    letter-spacing: 0.5px;
  }
  .wordmark-dot {
    width: 14px; height: 14px; border-radius: 50%;
    background: var(--brand-red);
  }
  .header-rule {
    position: absolute; top: 98px; left: 10px; width: 280px; height: 1px;
    background: linear-gradient(90deg, transparent, var(--rule-grey), transparent);
  }
  .offer {
    position: absolute; top: 124px; left: 0; width: 300px;
    text-align: center; font-weight: 600; font-size: 19px; line-height: 37px;
    margin: 0;
  }
  .offer .accent { color: var(--brand-red); }
  .cta {
    position: absolute; top: 245px; left: 79px;
    width: 139px; height: 36px;
    background: var(--brand-red); color: var(--white);
    display: flex; align-items: center; justify-content: center;
    font-size: 13px; font-weight: 600; text-transform: uppercase;
    text-decoration: none;
  }
  .red-band {
    position: absolute; left: 0; top: 0; width: 300px; height: 600px;
  }
  .tyre-photo {
    position: absolute; left: 75px; top: 318px;
    width: 160px; height: 225px;
    border-radius: 46% 50% 50% 46% / 50%;
    background: radial-gradient(ellipse at 62% 50%, #8a8a8a 0%, #4a4a4a 22%, #1d1d1d 40%, #2c2c2c 70%, #101010 100%);
    box-shadow: 0 18px 18px -6px rgba(0,0,0,0.55);
  }
  .brands { position: absolute; top: 0; left: 0; margin: 0; padding: 0; list-style: none; }
  .brand {
    position: absolute; width: 56px; margin-left: -28px;
    display: flex; flex-direction: column; align-items: center; gap: 2px;
    font-size: 6px; font-weight: 600; text-transform: uppercase; letter-spacing: 0.3px;
  }
  .brand-dot {
    width: 16px; height: 16px; border-radius: 50%;
    border: 1.5px solid var(--white); box-sizing: border-box;
  }
  .contact {
    position: absolute; top: 567px; left: 18px; right: 19px;
    display: flex; justify-content: space-between;
    font-size: 12px; font-weight: 600; letter-spacing: 0.8px;
  }
</style>
</head>
<body>
  <section class="ad" aria-label="Wheel Mates tyre advert">
    <div class="tread-backdrop" role="img" aria-label="Dark stacked tyre treads in the background"></div>

    <div class="wordmark"><span class="wordmark-dot"></span>Wheel Mates</div>
    <div class="header-rule"></div>

    <p class="offer">
      <span class="accent">FREE</span> INSTALLATION<br>
      KYD<span class="accent">$55-60</span><br>
      <span class="accent">Bulk</span> and individually
    </p>

    <a class="cta" href="#">Learn more</a>

    <svg class="red-band" viewBox="0 0 300 600" aria-hidden="true">
      <polygon points="0,518 300,455 300,468 0,525" fill="#ffffff"/>
      <polygon points="0,525 300,478 300,600 0,600" fill="var(--brand-red)"/>
    </svg>

    <div class="tyre-photo" role="img" aria-label="Passenger car tyre mounted on a grey alloy wheel"></div>

    <ul class="brands">
      <li class="brand" style="left:35px;top:316px"><span class="brand-dot"></span>Vardo</li>
      <li class="brand" style="left:35px;top:353px"><span class="brand-dot"></span>Strandmobil</li>
      <li class="brand" style="left:35px;top:387px"><span class="brand-dot"></span>Bexiline</li>
      <li class="brand" style="left:35px;top:423px"><span class="brand-dot"></span>Pelmoro</li>
      <li class="brand" style="left:35px;top:457px"><span class="brand-dot"></span>Korvexa</li>
      <li class="brand" style="left:261px;top:315px"><span class="brand-dot"></span>Ravello</li>
      <li class="brand" style="left:261px;top:352px"><span class="brand-dot"></span>Talvo</li>
      <li class="brand" style="left:261px;top:388px"><span class="brand-dot"></span>Pip</li>
      <li class="brand" style="left:261px;top:422px"><span class="brand-dot"></span>Quendra</li>
    </ul>

    <footer class="contact">
      <span class="phone">+1 345 555 0187</span>
      <span class="web">wheelmates-demo.ky</span>
    </footer>
  </section>
</body>
</html>
```